Launching a consulting business

I need a business card to launch a new consulting business. I provide executive level consultation throughout New York state to CEO and ED's who run and manage non-fo-profit corporations who support individuals with intellectual and developmental disabilities. The field is undergoing an evolution from a social model of care to more outcome based strategies. Having expertise in health care, leading a $50M business providing this service and working in the government creating policy I can bring to the Executive and corporations compassion, vision, strategy with a clear understanding of business practices for success. The field is moving to managed care. My background in health care management brings the expertise to create opportunities and possibilities. I currently have three projects I am consulting on - 1. Field expert assisting an accounting firm in the creation of a managed care application to become a managed care company supporting the ID/DD field. I crafted the care management model 2. Strategizing on product line creation to assure an agency is ready with a compendium services supporting the ID/DD field. 3. Facilitating a financial model to assist in predicting costs to render services in ID/DD. Developing and overlaying outcome measures to position agencies for effective marketing.
Quality is my passion and assuring all people live their life's dreams.
I would also like a template for letterhead stationary following what is created with my business card.
I wold like to incorporate a cranberry/sage tartan plaid within the design.

Please note my last name is spelled wrong on the attachment. I also do not want the tartan plaid used covering the entire card. i open to other ideas and suggestions.

Industry/Entity Type

Government

Contact Information for Business Card

Denise M Forbush
Phone - 845-562-7183
Cell phone 845-734-2096
Email address - denisemfor@quillpost.com

```html
<!DOCTYPE html>
<html lang="en">
<head>
<meta charset="utf-8">
<title>Denise M Forbush — Business Card</title>
<link rel="stylesheet" href="https://fonts.googleapis.com/css2?family=Open+Sans:wght@400;600&display=swap">
<style>
  :root {
    --coral: #f07470;
    --teal: #74bfb9;
    --sage: #849a8c;
    --paper: #ffffff;
    --backdrop: #dcdddb;
  }
  html, body {
    margin: 0;
    padding: 0;
    width: 1200px;
    height: 1000px;
    overflow: hidden;
    background: var(--backdrop);
  }
  .canvas {
    position: relative;
    width: 1200px;
    height: 1000px;
  }
  .business-card {
    position: absolute;
    left: 100px;
    top: 215px;
    width: 1000px;
    height: 569px;
    background: var(--paper);
    font-family: "Open Sans", Arial, sans-serif;
    box-shadow: 0 4px 14px rgba(0,0,0,0.12);
  }
  .identity {
    position: absolute;
    right: 345px;
    text-align: right;
    white-space: nowrap;
  }
  .name {
    top: 112px;
    margin: 0;
    font-size: 61px;
    font-weight: 600;
    letter-spacing: 2px;
    color: var(--coral);
    line-height: 1;
  }
  .role {
    top: 182px;
    margin: 0;
    font-size: 26px;
    font-weight: 400;
    letter-spacing: 1px;
    color: var(--teal);
    line-height: 1;
  }
  .contact-list {
    top: 318px;
    margin: 0;
    padding: 0;
    list-style: none;
    font-size: 35px;
    letter-spacing: 1.5px;
    line-height: 47.5px;
  }
  .contact-value { color: var(--coral); }
  .contact-label { color: var(--teal); }
  .plaid-panel {
    position: absolute;
    right: 0;
    top: 0;
    width: 306px;
    height: 569px;
    background: linear-gradient(180deg,
      var(--teal) 0%,
      var(--sage) 25%,
      var(--coral) 50%,
      var(--sage) 75%,
      var(--teal) 100%);
  }
</style>
</head>
<body>
<div class="canvas">
  <section class="business-card">
    <h1 class="identity name">Denise M Forbush</h1>
    <p class="identity role">Executive Business Strategy Consultant</p>
    <ul class="identity contact-list">
      <li><span class="contact-value">845-562-7183</span> <span class="contact-label">(tel)</span></li>
      <li><span class="contact-value">845-734-2096</span> <span class="contact-label">(cell)</span></li>
      <li><span class="contact-value">denisemfor@quillpost.com</span> <span class="contact-label">(email)</span></li>
    </ul>
    <div class="plaid-panel" role="img" aria-label="Cranberry, sage and teal striped tartan band"></div>
  </section>
</div>
</body>
</html>
```